Business card design needed

My business is in Matchmaking. My objective is to find the most compatible partner for my clients....basically I'm in the love and happiness industry bringing two people together for a lasting loving relationship.

I envision the design to be something with 2 people who are in love looking happy or even a silhouette.....I don't really know, I'm open to ideas.....maybe no picture at all, but I want it to be classy :-)

I do have a logo which I will upload. You can also go to my website to give you an idea on the colours and the design if that helps, however the website is not finished yet, it should be up by today or tomorrow. If the website has a heart with swirls on the upper left hand corner, that is the old website, please ignore that one. The one that will be up shortly has a picture frame on the home page with my logo that will be in the file I will upload on this page.

Target Market(s)

There are three categories: Over 45, Asian and Western and same sex, but would be able to afford to hire a matchmaker

Contact Information for Business Card

The Tide Lantern
Helping You Find The "One"
Mira Feltham
Matchmaker
0472 915 264
info@thetidelantern.com.au
www.thetidelantern.com.au

```html
<!DOCTYPE html>
<html lang="en">
<head>
<meta charset="utf-8">
<title>The Tide Lantern – Business Card</title>
<link rel="stylesheet" href="https://fonts.googleapis.com/css2?family=Open+Sans:wght@600&family=Cormorant+Garamond:wght@500&display=swap">
<style>
  :root {
    --page-bg: #e9e9ea;
    --card-bg: #030305;
    --magenta: #c2257f;
    --cyan: #1fa3bf;
    --contact: #e8d9c4;
  }
  * { margin: 0; padding: 0; box-sizing: border-box; }
  html, body {
    width: 1120px;
    height: 1200px;
    overflow: hidden;
    background: var(--page-bg);
  }
  .canvas {
    width: 1120px;
    height: 1200px;
    display: flex;
    align-items: center;
    justify-content: center;
  }
  .card {
    position: relative;
    width: 660px;
    height: 1080px;
    background: var(--card-bg);
    overflow: hidden;
    box-shadow: 0 10px 30px rgba(0,0,0,0.25);
  }
  .card__header {
    position: absolute;
    top: 82px;
    left: 0;
    right: 0;
    text-align: center;
    font-family: "Open Sans", sans-serif;
    font-weight: 600;
    color: var(--magenta);
    font-size: 34px;
    line-height: 1.05;
    letter-spacing: 0.5px;
    text-transform: uppercase;
  }
  .brand {
    position: absolute;
    top: 292px;
    left: 0;
    right: 0;
    display: flex;
    align-items: center;
    justify-content: center;
    gap: 18px;
  }
  .brand__dot {
    width: 30px;
    height: 30px;
    border-radius: 50%;
    background: var(--magenta);
  }
  .brand__name {
    font-family: "Open Sans", sans-serif;
    font-weight: 600;
    font-size: 50px;
    color: var(--cyan);
  }
  .tagline {
    position: absolute;
    top: 382px;
    left: 0;
    right: 0;
    text-align: center;
    font-family: "Open Sans", sans-serif;
    font-weight: 600;
    font-size: 19px;
    color: var(--cyan);
    text-transform: uppercase;
    letter-spacing: 0.3px;
  }
  .light-field {
    position: absolute;
    left: 0;
    right: 0;
    top: 430px;
    height: 520px;
    background: linear-gradient(180deg,
      rgba(3,3,5,0) 0%,
      rgba(18,70,115,0.35) 22%,
      rgba(38,140,200,0.55) 42%,
      rgba(90,50,180,0.5) 60%,
      rgba(140,40,125,0.35) 80%,
      rgba(3,3,5,0) 100%);
  }
  .contact {
    position: absolute;
    right: 48px;
    bottom: 96px;
    text-align: right;
    font-family: "Cormorant Garamond", serif;
    font-style: normal;
    font-weight: 500;
    font-size: 22px;
    line-height: 1.35;
    color: var(--contact);
    text-transform: uppercase;
    letter-spacing: 0.4px;
  }
</style>
</head>
<body>
<main class="canvas">
  <article class="card">
    <header class="card__header">
      <div class="card__person">Mira Feltham</div>
      <div class="card__role">Matchmaker</div>
    </header>

    <div class="brand">
      <span class="brand__dot"></span>
      <span class="brand__name">The Tide Lantern</span>
    </div>
    <p class="tagline">The Tide Lantern helping you find the “One”</p>

    <div class="light-field" role="img" aria-label="Artwork of flowing blue, violet and pink light across the card"></div>

    <address class="contact">
      <div class="contact__phone">Phone - 0472 915 264</div>
      <div class="contact__email">Email - info@thetidelantern.com.au</div>
      <div class="contact__web">Web - www.thetidelantern.com.au</div>
    </address>
  </article>
</main>
</body>
</html>
```